Energy Company needs a Business Card Design

We need a business card design for a new company based in Singapore called Velmora Energy. Velmora Energy is a producer of renewable energies largely for the biofuels market. Sourced entirely from sustainable resources, Velmora Energy aims to be a fully integrated oil company operating in 100% sustainable way. We would like to see designs that use the same colours as the attached file.

Industry/Entity Type

Business

```html
<!DOCTYPE html>
<html lang="en">
<head>
<meta charset="utf-8">
<title>Velmora Energy – Business Card</title>
<link href="https://fonts.googleapis.com/css2?family=Montserrat:wght@400;500;700&display=swap" rel="stylesheet">
<style>
  :root {
    --bg: #e4e4e2;
    --card: #ffffff;
    --green: #7cc423;
    --grey-text: #8a8a8a;
    --ink: #3a3a3a;
    --swoosh-light: #f4f4f4;
    --swoosh-dark: #d9d9d9;
  }
  * { box-sizing: border-box; margin: 0; padding: 0; }
  html, body {
    width: 1200px; height: 900px; overflow: hidden;
    background: var(--bg);
    font-family: "Montserrat", sans-serif;
  }
  .sheet {
    position: relative; width: 1200px; height: 900px;
    display: flex; flex-direction: column; align-items: center;
    justify-content: center; gap: 50px;
  }
  .card {
    position: relative; width: 660px; height: 377px;
    background: var(--card); border-radius: 26px; overflow: hidden;
    box-shadow: 0 6px 18px rgba(0,0,0,0.12);
  }
  .brand {
    display: flex; align-items: center; gap: 14px;
  }
  .brand-dot {
    width: 22px; height: 22px; border-radius: 50%; background: var(--green); flex: none;
  }
  .brand-name {
    color: var(--grey-text); font-weight: 700; font-size: 50px;
    letter-spacing: 1px; line-height: 1; white-space: nowrap;
  }
  /* back: centred brand */
  .card--back { display: flex; align-items: center; justify-content: center; }

  /* front: brand + contact over swoosh */
  .card--front .swoosh { position: absolute; left: 0; top: 0; width: 100%; height: 100%; }
  .card--front .brand { position: absolute; left: 30px; top: 135px; gap: 10px; }
  .card--front .brand-dot { width: 18px; height: 18px; }
  .card--front .brand-name { font-size: 31px; letter-spacing: 0.5px; }
  .contact {
    position: absolute; left: 392px; top: 40px; color: var(--ink);
  }
  .contact-name { color: var(--green); font-weight: 700; font-size: 21px; letter-spacing: 0.5px; }
  .contact-role { font-size: 13px; letter-spacing: 1px; margin-top: 2px; }
  .contact-address { font-size: 13px; letter-spacing: 1px; line-height: 1.35; margin-top: 20px; }
  .contact-lines { list-style: none; margin-top: 6px; }
  .contact-lines li {
    display: flex; align-items: center; gap: 10px;
    font-size: 13px; letter-spacing: 0.8px; line-height: 1.6; white-space: nowrap;
  }
  .contact-icon { width: 15px; height: 15px; flex: none; }
</style>
</head>
<body>
<main class="sheet">

  <section class="card card--back" aria-label="Card back">
    <div class="brand">
      <span class="brand-dot"></span>
      <span class="brand-name">Velmora Energy</span>
    </div>
  </section>

  <section class="card card--front" aria-label="Card front">
    <svg class="swoosh" viewBox="0 0 660 377" preserveAspectRatio="none" aria-hidden="true">
      <defs>
        <linearGradient id="swooshFill" x1="0" y1="0" x2="0" y2="1">
          <stop offset="0" stop-color="var(--swoosh-light)"/>
          <stop offset="1" stop-color="var(--swoosh-dark)"/>
        </linearGradient>
      </defs>
      <path d="M0 340 C140 272 300 278 430 275 C560 272 630 255 660 215 L660 377 L0 377 Z" fill="url(#swooshFill)"/>
      <path d="M0 340 C140 272 300 278 430 275 C560 272 630 255 660 215" fill="none" stroke="var(--green)" stroke-width="4"/>
    </svg>

    <div class="brand">
      <span class="brand-dot"></span>
      <span class="brand-name">Velmora Energy</span>
    </div>

    <div class="contact">
      <p class="contact-name">Daniel Reyes</p>
      <p class="contact-role">President</p>
      <p class="contact-address">48 Harbour Lane<br>Eastfield, AB 20417</p>
      <ul class="contact-lines">
        <li>
          <svg class="contact-icon" viewBox="0 0 16 16" aria-hidden="true"><circle cx="8" cy="8" r="8" fill="var(--green)"/><rect x="5.5" y="3.5" width="5" height="9" rx="1" fill="#fff"/></svg>
          +1555. 310. 482
        </li>
        <li>
          <svg class="contact-icon" viewBox="0 0 16 16" aria-hidden="true"><circle cx="8" cy="8" r="8" fill="var(--green)"/><path d="M5 4.5c0 4 2.5 6.5 6.5 6.5l.5-1.8-2-.8-.9 1c-1.3-.6-2.2-1.5-2.8-2.8l1-.9-.8-2z" fill="#fff"/></svg>
          +1555. 310. 496
        </li>
        <li>
          <svg class="contact-icon" viewBox="0 0 16 16" aria-hidden="true"><circle cx="8" cy="8" r="8" fill="var(--green)"/><rect x="4" y="5" width="8" height="6" fill="#fff"/><path d="M4 5l4 3.2L12 5" fill="none" stroke="var(--green)" stroke-width="1"/></svg>
          info@velmoraenergy.com
        </li>
        <li>
          <svg class="contact-icon" viewBox="0 0 16 16" aria-hidden="true"><circle cx="8" cy="8" r="8" fill="var(--green)"/><circle cx="8" cy="8" r="4" fill="none" stroke="#fff" stroke-width="1"/><path d="M4 8h8M8 4c-2 2.5-2 5.5 0 8M8 4c2 2.5 2 5.5 0 8" fill="none" stroke="#fff" stroke-width="0.9"/></svg>
          www.velmoraenergy.com
        </li>
      </ul>
    </div>
  </section>

</main>
</body>
</html>
```